A modern web page for a software product

We need a web page for a software product, which is an advanced solution based on Machine Learning and Natural Language processing. We already have a logo of the product and expect the web page to be inline with the logo colors. The design should be for one page web site with scrolled sections - details of the content and guidelines in the attachments.

Target Market(s)

software company

Industry/Entity Type

It Company

Number of Pages Required

1 page

Colors

Designer to choose colors to be used in the design.

Requirements
Must have
• - modern icons and graphics
• - inline with the logo colors
• - be related to Machine Learining, AI, data processing
• - should have two language versions: english and polish both are attached.
Nice to have
• - animation/motion
Should not have
• - any photos embedded

```html
<!DOCTYPE html>
<html lang="en">
<head>
<meta charset="utf-8">
<title>Sortlane – Advanced and Secured Data Processing</title>
<link href="https://fonts.googleapis.com/css2?family=Poppins:wght@600;700&family=Open+Sans:wght@400;600;700&family=Teko:wght@400;500&family=Libre+Baskerville&display=swap" rel="stylesheet">
<style>
:root{
  --hero-top:#8fa0fa;
  --hero-bottom:#6a5cf0;
  --teal:#14b3ae;
  --teal-dark:#0b7275;
  --navy:#173a6e;
  --ink:#2b2b2b;
  --muted:#555;
  --grey-band:#ebebeb;
  --light-band:#f2f5f7;
  --white:#fff;
  --nav-active:#ffd84a;
  --line:#d6d6d6;
}
*{box-sizing:border-box;margin:0;padding:0}
html,body{width:1200px;height:3087px;overflow:hidden}
body{position:relative;font-family:"Open Sans",Arial,sans-serif;color:var(--ink);background:var(--white)}
.abs{position:absolute}

/* hero */
.hero{position:absolute;left:0;top:0;width:1200px;height:685px;background:linear-gradient(160deg,var(--hero-top),var(--hero-bottom));overflow:hidden}
.hero-decor{position:absolute;left:0;top:0}
.brand{position:absolute;left:98px;top:22px;display:flex;align-items:center;gap:12px;font-family:"Poppins",sans-serif;font-weight:700;font-size:30px;color:var(--white)}
.brand-dot{width:22px;height:22px;border-radius:50%;background:var(--teal)}
.main-nav{position:absolute;right:100px;top:28px;display:flex;gap:32px;font-size:13px;font-weight:700;color:var(--white)}
.main-nav .active{color:var(--nav-active)}
.hero-title{position:absolute;left:0;width:1200px;top:94px;text-align:center;font-family:"Poppins",sans-serif;font-weight:700;font-size:35px;color:var(--white)}
.hero-lead{position:absolute;left:270px;width:660px;top:166px;text-align:center;font-family:Georgia,serif;font-size:15px;line-height:26px;color:#eef0ff}
.btn-outline{position:absolute;left:603px;top:245px;width:138px;height:41px;border:1.5px solid var(--white);border-radius:21px;color:var(--white);font-size:11px;font-weight:600;display:flex;align-items:center;justify-content:center;letter-spacing:.5px}
.hero-visual{position:absolute;left:313px;top:320px;width:576px;height:320px;border-radius:10px;background:linear-gradient(135deg,#eef2fb,#c9d4ee);border:14px solid var(--white);box-shadow:0 10px 30px rgba(40,30,120,.25)}

/* section headings */
.section-title{position:absolute;left:0;width:1200px;text-align:center;font-family:"Teko",sans-serif;font-weight:500;font-size:46px;letter-spacing:.5px;color:#1d1d1d}

/* icon tile */
.ico{position:absolute;width:40px;height:40px;border:3px solid var(--teal);border-radius:6px}
.ico-sm{width:34px;height:34px}

/* features */
.feature-title{position:absolute;font-weight:700;font-size:18px;line-height:26px;color:#222}
.ticks{position:absolute;list-style:none;font-size:15px;line-height:22px;color:#333}
.ticks li{position:relative;padding-left:36px;margin-bottom:17px}
.ticks li svg{position:absolute;left:0;top:2px}

/* use cases */
.usecases-band{position:absolute;left:0;top:1240px;width:1200px;height:480px}
.use-text{position:absolute;font-size:15px;line-height:21px;color:#333}

/* highlights */
.highlights-band{position:absolute;left:0;top:1708px;width:1200px;height:504px;background:var(--light-band)}
.card{position:absolute;width:241px;background:var(--white);border:2px solid var(--line)}
.card-title{position:absolute;left:38px;right:20px;font-weight:700;font-size:16px;line-height:23px;color:#222}
.card-visual{position:absolute;border-radius:8px;background:var(--teal)}
.btn-more{position:absolute;left:50px;bottom:-10px;width:134px;height:26px;background:var(--navy);color:var(--white);font-size:15px;display:flex;align-items:center;justify-content:center;letter-spacing:.5px}

/* contact */
.contact-band{position:absolute;left:0;top:2212px;width:1200px;height:663px;background:var(--navy)}
.contact-panel{position:absolute;left:138px;top:2297px;width:961px;height:539px;background:var(--white)}
.contact-card{position:absolute;left:95px;top:2340px;width:444px;height:455px;background:var(--teal-dark);color:var(--white);font-family:"Libre Baskerville",Georgia,serif;box-shadow:0 6px 16px rgba(0,0,0,.25)}
.contact-card h2{position:absolute;left:44px;top:38px;font-weight:400;font-size:27px}
.contact-col{position:absolute;font-size:13px;line-height:26px}
.contact-col u{text-decoration:underline}
.form-title{position:absolute;left:583px;top:2378px;font-family:"Libre Baskerville",Georgia,serif;font-size:29px;color:#111}
.field{position:absolute;border:1.5px solid var(--line);font-size:12px;color:#aaa;padding:11px 10px}
.btn-send{position:absolute;left:585px;top:2711px;width:156px;height:42px;background:var(--navy);color:var(--white);font-size:11px;font-weight:700;display:flex;align-items:center;justify-content:center}

/* footer */
.footer{position:absolute;left:0;top:2875px;width:1200px;height:212px;background:#f7f7f7}
.footer-nav{position:absolute;left:0;width:1200px;top:44px;text-align:center;font-size:27px;color:#111;letter-spacing:.3px}
.footer-nav span{margin:0 14px}
.social{position:absolute;top:132px;left:0;width:1200px;display:flex;justify-content:center;gap:34px}
.social a{display:flex;align-items:center;gap:8px;font-size:14px;font-weight:600;color:#444;text-decoration:none}
.social i{display:block;width:20px;height:20px;border-radius:50%;border:2px solid #888}
.social-rule{position:absolute;top:154px;height:1px;background:#bbb}
</style>
</head>
<body>

<svg width="0" height="0" style="position:absolute">
  <defs>
    <symbol id="tick" viewBox="0 0 20 20"><path d="M3 10 l5 5 L17 4" fill="none" stroke="#14b3ae" stroke-width="3" stroke-linecap="round" stroke-linejoin="round"/></symbol>
  </defs>
</svg>

<!-- Hero -->
<header class="hero">
  <svg class="hero-decor" width="1200" height="685">
    <circle cx="1150" cy="300" r="170" fill="#ffffff" opacity=".07"/>
    <circle cx="70" cy="470" r="110" fill="#ffffff" opacity=".06"/>
    <path d="M0 560 C150 500 260 620 420 570 S760 520 900 580 S1100 540 1200 560 V685 H0Z" fill="#ffffff" opacity=".08"/>
    <path d="M0 610 C200 570 330 650 520 620 S880 590 1040 630 S1160 600 1200 610 V685 H0Z" fill="#ffffff" opacity=".1"/>
  </svg>
  <div class="brand"><span class="brand-dot"></span>Sortlane</div>
  <nav class="main-nav"><span class="active">HOME</span><span>Features</span><span>Used Cases</span><span>Highlight</span><span>Contact</span>
    <svg width="13" height="13" viewBox="0 0 14 14"><circle cx="6" cy="6" r="4.5" fill="none" stroke="#fff" stroke-width="2"/><path d="M9.5 9.5 L13 13" stroke="#fff" stroke-width="2"/></svg></nav>
  <h1 class="hero-title">Advanced and Secured Date Processing</h1>
  <p class="hero-lead">Lorem ipsum dolor sit amet, consectetuer adipiscing elit. Aenean commodo ligula eget dolor. Aenean massa. Cum sociis natoque penatibus et magnis dis parturient montes,</p>
  <div class="btn-outline">LEARN MORE</div>
  <div class="hero-visual" role="img" aria-label="Laptop showing a circuit-board style data network graphic"></div>
</header>

<!-- Main features -->
<section>
  <h2 class="section-title" style="top:722px">MAIN FEATURES</h2>

  <div class="ico" style="left:97px;top:848px" role="img" aria-label="Safe icon"></div>
  <div class="feature-title" style="left:156px;top:838px;width:240px">Detection of personal &amp; sensitive data for GDPR compliance</div>
  <ul class="ticks" style="left:118px;top:943px;width:300px">
    <li><svg width="20" height="20"><use href="#tick"/></svg>in structural sources<br>(e.g. SQL servers)</li>
    <li><svg width="20" height="20"><use href="#tick"/></svg>in unstructured sources (e.g.: docs, e-mails, logs, data streams)</li>
    <li><svg width="20" height="20"><use href="#tick"/></svg>in "noisy" content written in natural language (e.g.: containing errors or custom formats)</li>
    <li><svg width="20" height="20"><use href="#tick"/></svg>built in ML models and rules for personal data used in Poland</li>
  </ul>

  <div class="ico" style="left:465px;top:840px" role="img" aria-label="Stopwatch icon"></div>
  <div class="feature-title" style="left:530px;top:835px;width:210px">Fast cataloging and classification of data and sources</div>
  <div class="ico" style="left:470px;top:990px" role="img" aria-label="Document with gear icon"></div>
  <div class="feature-title" style="left:530px;top:985px;width:210px">Unified data registry for RODO compliance fulfilment</div>
  <div class="ico" style="left:470px;top:1138px" role="img" aria-label="Network nodes icon"></div>
  <div class="feature-title" style="left:530px;top:1135px;width:210px">Management of consents and data access policies</div>

  <div class="ico" style="left:801px;top:836px" role="img" aria-label="Clipboard with check icon"></div>
  <div class="feature-title" style="left:859px;top:835px;width:250px">Customizable analytics and reporting</div>
  <div class="ico" style="left:801px;top:983px" role="img" aria-label="Tile grid icon"></div>
  <div class="feature-title" style="left:862px;top:970px;width:250px">Ability to integrates with tools for data anonymization or depersonalization</div>
  <div class="ico" style="left:801px;top:1140px" role="img" aria-label="API window icon"></div>
  <div class="feature-title" style="left:862px;top:1135px;width:250px">RESTful API for system management and integration</div>
</section>

<!-- Use cases -->
<section>
  <svg class="usecases-band" width="1200" height="480" viewBox="0 0 1200 480">
    <path d="M0 14 C200 0 400 24 600 10 S1000 0 1200 12 V440 C1000 460 800 430 600 446 S200 462 0 446Z" fill="#ebebeb"/>
  </svg>
  <h2 class="section-title" style="top:1282px">USE CASES</h2>

  <div class="ico" style="left:97px;top:1376px" role="img" aria-label="Checklist icon"></div>
  <div class="use-text" style="left:168px;top:1370px;width:240px">Internal audits &amp;verification of the current status - in preparation for ensuring RODO compliance RODO</div>
  <div class="ico ico-sm" style="left:97px;top:1522px" role="img" aria-label="Database icon"></div>
  <div class="use-text" style="left:168px;top:1518px;width:230px">Cataloging sources that store sensitive data</div>

  <div class="ico ico-sm" style="left:461px;top:1373px" role="img" aria-label="Registry icon"></div>
  <div class="use-text" style="left:526px;top:1366px;width:270px">Keeping the registry of personal data in order to implement rights to information, forgetfulness, data transfer</div>
  <div class="ico ico-sm" style="left:461px;top:1524px" role="img" aria-label="Monitor icon"></div>
  <div class="use-text" style="left:526px;top:1524px;width:260px">Continuous monitoring and classification of data</div>

  <div class="ico ico-sm" style="left:852px;top:1370px" role="img" aria-label="Stacked documents icon"></div>
  <div class="use-text" style="left:925px;top:1358px;width:240px">Use collected the data to create additional business value, e.g.:</div>
  <ul class="ticks" style="left:900px;top:1442px;width:240px;font-size:15px">
    <li style="margin-bottom:4px"><svg width="18" height="18"><use href="#tick"/></svg>classification of documents,</li>
    <li style="margin-bottom:4px"><svg width="18" height="18"><use href="#tick"/></svg>analysis of sentiment,</li>
    <li style="margin-bottom:4px"><svg width="18" height="18"><use href="#tick"/></svg>customer analytics for marketing,</li>
    <li style="margin-bottom:4px"><svg width="18" height="18"><use href="#tick"/></svg>fraud detection,<br>data governance</li>
  </ul>
</section>

<!-- Highlights -->
<section class="highlights-band">
  <h2 class="section-title" style="top:52px">HIGHLIGHTS</h2>

  <div class="card" style="left:95px;top:167px;height:286px">
    <div class="card-visual" style="left:78px;top:38px;width:80px;height:90px" role="img" aria-label="Document with gear icon"></div>
    <div class="card-title" style="top:166px">Built in support for detection of Polish personal data</div>
    <div class="btn-more">READ MORE</div>
  </div>
  <div class="card" style="left:350px;top:167px;height:286px">
    <div class="card-visual" style="left:78px;top:34px;width:80px;height:100px" role="img" aria-label="AI robot illustration"></div>
    <div class="card-title" style="top:162px;left:18px">High effectiveness of person AI data detection (also "noisy" data) by combining:</div>
    <div class="btn-more">READ MORE</div>
  </div>
  <div class="card" style="left:605px;top:167px;height:286px">
    <svg style="position:absolute;left:80px;top:36px" width="80" height="94" viewBox="0 0 80 94" role="img" aria-label="Database icon">
      <g fill="none" stroke="#14b3ae" stroke-width="6"><ellipse cx="40" cy="14" rx="34" ry="11"/><path d="M6 14 V80 C6 94 74 94 74 80 V14"/><path d="M6 36 C6 50 74 50 74 36"/><path d="M6 58 C6 72 74 72 74 58"/></g>
    </svg>
    <div class="card-title" style="top:186px;left:14px">Supports structured &amp; unstructured data source</div>
    <div class="btn-more">READ MORE</div>
  </div>
  <div class="card" style="left:860px;top:-12px;height:465px">
    <div class="card-visual" style="left:68px;top:28px;width:90px;height:90px;border-radius:50%" role="img" aria-label="Speedometer performance icon"></div>
    <div class="card-title" style="top:170px;left:14px">Ready for high performance processing</div>
    <ul class="ticks" style="left:14px;top:245px;width:220px;font-size:15px">
      <li style="margin-bottom:14px"><svg width="18" height="18"><use href="#tick"/></svg>handles TBs of data easily</li>
      <li style="margin-bottom:14px"><svg width="18" height="18"><use href="#tick"/></svg>linear scalability</li>
      <li><svg width="18" height="18"><use href="#tick"/></svg>high availability<br>and DRC deployments</li>
    </ul>
    <div class="btn-more">READ MORE</div>
  </div>
</section>

<!-- Contact -->
<section>
  <div class="contact-band"></div>
  <div class="contact-panel"></div>
  <div class="contact-card">
    <h2>Our Contacts</h2>
    <div class="contact-col" style="left:44px;top:98px">Our Address<br>218 Alder Quay Suite,<br>CA 90417<br><u>info@vellarion.com</u></div>
    <div class="contact-col" style="left:256px;top:98px">Sales<br>Marta Kessling<br>Press Relations<br><u>careers@vellarion.com</u></div>
    <div class="contact-col" style="left:44px;top:252px">Email<br>hello@sortlane.io</div>
  </div>
  <h2 class="form-title">Get in Touch</h2>
  <div class="field" style="left:585px;top:2432px;width:230px;height:42px">First Name</div>
  <div class="field" style="left:823px;top:2432px;width:232px;height:42px">Last Name</div>
  <div class="field" style="left:585px;top:2484px;width:230px;height:42px">Email Address</div>
  <div class="field" style="left:823px;top:2484px;width:232px;height:42px">Phone Number</div>
  <div class="field" style="left:585px;top:2536px;width:470px;height:148px">Write Your Message Here…</div>
  <div class="btn-send">SEND MESSAGE</div>
</section>

<!-- Footer -->
<footer class="footer">
  <nav class="footer-nav"><span>HOME</span>|<span>USE CASES</span>|<span>MAIN FEATURES</span>|<span>HIGHLIGHT</span>|<span>CONTACTS</span></nav>
  <div class="social-rule" style="left:420px;width:30px"></div>
  <div class="social-rule" style="left:750px;width:30px"></div>
  <div class="social">
    <a><i></i>Chirply</a>
    <a><i></i>Facenook</a>
    <a><i></i>Orbitly</a>
    <a><i></i>Pinboardy</a>
  </div>
</footer>

</body>
</html>
```